front and back labels on a single sheet.

Vodka label design
Vodka is a colourless liquor. This vodka is tasteless and with no flavour.

FRONT LABEL
"CORVEN FIELD" is the brand name . it should be as big as possible.
below that " Only vodka made from sustainable means"
Remaining details to be copied from attached file.
Back Label
Details attached.

Colors
00AB8E
00BBA5
67D7C9
C6EFE9
E9F9F6

```html
<!DOCTYPE html>
<html lang="en">
<head>
<meta charset="utf-8">
<title>Corven Field Vodka – Front and Back Labels</title>
<link href="https://fonts.googleapis.com/css2?family=Poppins:wght@400;500;600;700;800&display=swap" rel="stylesheet">
<style>
  :root {
    --sheet-bg: #d6d6d6;
    --label-white: #ffffff;
    --pattern-grey: #ededed;
    --ink: #262626;
    --ink-soft: #4a4a4a;
    --brand-green: #2e8b2e;
    --leaf-green: #3a9d3a;
    --lime: #c3e04a;
    --dark-band: #2c2c2c;
    --warning-red: #d12b2b;
    --rule: #8a8a8a;
  }
  * { box-sizing: border-box; margin: 0; padding: 0; }
  html, body { width: 1200px; height: 728px; overflow: hidden; }
  body { background: var(--sheet-bg); font-family: "Poppins", sans-serif; color: var(--ink); }

  .sheet { position: relative; width: 1200px; height: 728px; }

  .label {
    position: absolute; top: 84px; width: 540px; height: 560px;
    background: var(--label-white);
    box-shadow: 0 6px 22px rgba(0,0,0,0.18);
    overflow: hidden;
  }
  .label--front { left: 40px; }
  .label--back { left: 620px; }

  .leaf-field {
    position: absolute; left: 0; right: 0;
    background: linear-gradient(180deg, #efefef 0%, var(--pattern-grey) 60%, #e8e8e8 100%);
  }
  .label--front .leaf-field { top: 150px; height: 282px; }
  .label--back .leaf-field { top: 130px; height: 302px; }

  .band { position: absolute; left: 0; right: 0; display: flex; align-items: center; justify-content: center; }
  .band--lime { top: 432px; height: 54px; background: var(--lime); }
  .band--dark { top: 486px; height: 74px; background: var(--dark-band); color: #fff; }

  /* front */
  .maker-mark { position: absolute; top: 46px; left: 0; right: 0; text-align: center; }
  .maker-mark__name {
    display: inline-flex; align-items: center; gap: 8px;
    font-weight: 700; font-size: 22px; letter-spacing: 0.5px; color: var(--brand-green);
  }
  .maker-mark__dot { width: 14px; height: 14px; border-radius: 50%; background: var(--leaf-green); }
  .maker-mark__tagline { margin-top: 4px; font-size: 7px; letter-spacing: 0.8px; color: var(--ink-soft); text-transform: uppercase; }

  .brand-name {
    position: absolute; left: 0; right: 0; text-align: center;
    font-weight: 800; line-height: 0.86; letter-spacing: -4px; text-transform: uppercase;
  }
  .brand-name__top { display: block; color: var(--ink); }
  .brand-name__bottom { display: block; color: var(--brand-green); }
  .label--front .brand-name { top: 176px; font-size: 108px; }

  .front-claim { position: absolute; top: 362px; left: 0; right: 0; text-align: center; text-transform: uppercase; line-height: 1.05; }
  .front-claim__small { font-weight: 600; font-size: 17px; }
  .front-claim__large { font-weight: 700; font-size: 28px; }

  .strength { font-weight: 700; font-size: 20px; letter-spacing: 3px; display: flex; align-items: center; gap: 16px; }
  .strength__divider { width: 2px; height: 26px; background: var(--ink); }
  .band-caption { font-weight: 600; font-size: 19px; letter-spacing: 5px; text-transform: uppercase; }

  /* back */
  .label--back .brand-name { top: 34px; font-size: 52px; letter-spacing: -2px; }

  .story { position: absolute; top: 150px; left: 40px; right: 40px; text-align: center; font-size: 11.5px; line-height: 1.35; }
  .story p + p { margin-top: 10px; }

  .notice-row {
    position: absolute; top: 248px; left: 40px; right: 40px; height: 64px;
    display: flex; align-items: center; gap: 16px;
    border-bottom: 1px solid var(--rule); padding-bottom: 6px;
  }
  .distiller-portrait {
    width: 56px; height: 56px; border-radius: 50%; flex: none;
    background: radial-gradient(circle at 50% 45%, #8a6a55 0%, #5b463a 60%, #3e3a38 100%);
    border: 3px solid #fff; box-shadow: 0 0 0 1px var(--ink);
  }
  .pregnancy { display: flex; align-items: center; gap: 6px; }
  .pregnancy__title { font-weight: 700; font-size: 8.5px; color: var(--warning-red); text-transform: uppercase; }
  .pregnancy__text { font-size: 7.5px; line-height: 1.2; color: var(--ink-soft); }
  .drinks-mark { width: 26px; height: 30px; border: 2px solid var(--ink); border-radius: 3px 3px 8px 8px; margin-left: auto; }

  .serving-box {
    position: absolute; top: 330px; left: 40px; width: 220px; height: 86px;
    border: 1px solid var(--ink-soft); border-radius: 6px; padding: 10px 12px;
    font-size: 9px; line-height: 1.3; text-align: justify;
  }
  .serving-box p + p { margin-top: 6px; }

  .distiller { position: absolute; top: 328px; left: 286px; right: 30px; font-size: 8.5px; line-height: 1.3; color: var(--ink-soft); text-transform: uppercase; }
  .distiller__head { font-weight: 700; color: var(--brand-green); }
  .distiller__head + span { display: block; margin-bottom: 8px; }

  .web-address { font-weight: 600; font-size: 19px; letter-spacing: 3px; }
</style>
</head>
<body>
<main class="sheet">

  <section class="label label--front" aria-label="Front label">
    <div class="leaf-field" role="img" aria-label="Faint grey leaf pattern background"></div>

    <div class="maker-mark">
      <div class="maker-mark__name"><span class="maker-mark__dot"></span>TALLOW CREEK</div>
      <div class="maker-mark__tagline">Spirits infused with natures spicy herbs</div>
    </div>

    <h1 class="brand-name">
      <span class="brand-name__top">Corven</span>
      <span class="brand-name__bottom">Field</span>
    </h1>

    <div class="front-claim">
      <div class="front-claim__small">Only vodka made from</div>
      <div class="front-claim__large">Sustainable means</div>
    </div>

    <div class="band band--lime">
      <div class="strength"><span>50% ABV</span><span class="strength__divider"></span><span>750ML</span></div>
    </div>
    <div class="band band--dark"><span class="band-caption">Premium quality vodka</span></div>
  </section>

  <section class="label label--back" aria-label="Back label">
    <div class="leaf-field" role="img" aria-label="Faint grey leaf pattern background"></div>

    <h2 class="brand-name">
      <span class="brand-name__top">Corven</span>
      <span class="brand-name__bottom">Field</span>
    </h2>

    <div class="story">
      <p>The only vodka in the whole world which has unique 5 spices, and distilled 3+1 times</p>
      <p>In addition this is the only vodka made from natural rainwater &amp; solar power, thus making it the only vodka that is sustainably manufactured.</p>
    </div>

    <div class="notice-row">
      <div class="distiller-portrait" role="img" aria-label="Portrait photo of the distiller"></div>
      <div class="pregnancy">
        <svg width="30" height="30" viewBox="0 0 30 30" aria-hidden="true">
          <circle cx="15" cy="15" r="12.5" fill="none" stroke="#262626" stroke-width="2.5"/>
          <line x1="6" y1="24" x2="24" y2="6" stroke="#262626" stroke-width="2.5"/>
        </svg>
        <div>
          <div class="pregnancy__title">Pregnancy warning</div>
          <div class="pregnancy__text">Alcohol can cause lifelong<br>harm to your baby</div>
        </div>
      </div>
      <svg width="30" height="28" viewBox="0 0 30 28" aria-hidden="true">
        <polygon points="15,3 27,25 3,25" fill="none" stroke="#262626" stroke-width="2"/>
        <circle cx="15" cy="17" r="3" fill="#262626"/>
      </svg>
      <div class="drinks-mark"></div>
    </div>

    <div class="serving-box">
      <p>This vodka has to be taken chilled with ice cubes</p>
      <p>Making cocktails with lime and orange is a wonderful experience.</p>
    </div>

    <div class="distiller">
      <span class="distiller__head">Fermented and distilled by</span>
      <span>Marlow J. Penhale<br>at Tallow Creek Pvt. Ltd.</span>
      <span class="distiller__head">Made in</span><br>
      <span>Elmsworth, Victoria<br>Australia</span>
    </div>

    <div class="band band--lime"><span class="web-address">www.tallowcreek.com.au</span></div>
    <div class="band band--dark"><span class="band-caption">Made from sugarcane</span></div>
  </section>

</main>
</body>
</html>
```